business card design and letterhead for a building inspection company. We have a pre-purchase building and pest inspection ( i inspect house before people purchase it)
Updates

Tilda has been so so responsive and good, i highly recommend her

Industry/Entity Type

Building

Contact Information for Business Card

audience, solicitor, real estate agent, mortgage brokerthe rest of the info will be in the attachement business card

```html
<!DOCTYPE html>
<html lang="en">
<head>
<meta charset="utf-8">
<title>Northgate Property Inspections – Business Card</title>
<link href="https://fonts.googleapis.com/css2?family=Lato:wght@400;700;900&display=swap" rel="stylesheet">
<style>
  :root {
    --brand-blue: #1a73bb;
    --ink: #111111;
    --card: #ffffff;
    --backdrop: #4a4a4a;
  }
  html, body {
    margin: 0;
    padding: 0;
    width: 1200px;
    height: 1000px;
    overflow: hidden;
    background: var(--backdrop);
    font-family: "Lato", Arial, sans-serif;
  }
  .stage {
    position: relative;
    width: 1200px;
    height: 1000px;
  }
  .card {
    position: absolute;
    background: var(--card);
    border-radius: 14px;
    overflow: hidden;
  }
  .card--front {
    left: 204px; top: 138px;
    width: 586px; height: 360px;
  }
  .card--back {
    left: 360px; top: 513px;
    width: 582px; height: 358px;
  }
  .brand {
    position: absolute;
    color: var(--brand-blue);
  }
  .brand__name {
    display: flex;
    align-items: center;
    font-weight: 900;
    line-height: 1.1;
    letter-spacing: 0.5px;
    white-space: nowrap;
  }
  .brand__words { display: block; }
  .brand__mark {
    background: var(--brand-blue);
    flex: none;
  }
  .brand__tagline {
    font-weight: 400;
    letter-spacing: 1.6px;
    white-space: nowrap;
  }

  /* Front */
  .card--front .brand {
    left: 0; right: 0; top: 120px;
    display: flex; flex-direction: column; align-items: center;
  }
  .card--front .brand__name { font-size: 30px; gap: 16px; }
  .card--front .brand__mark { width: 34px; height: 34px; }
  .card--front .brand__tagline { font-size: 14px; margin-top: 8px; padding-left: 50px; }
  .services {
    position: absolute;
    left: 0; right: 0; top: 278px;
    margin: 0;
    text-align: center;
    color: var(--brand-blue);
    font-weight: 700;
    font-size: 16px;
    letter-spacing: 0.3px;
  }

  /* Back */
  .card--back .brand { left: 24px; top: 62px; }
  .card--back .brand__name { font-size: 21px; gap: 12px; }
  .card--back .brand__mark { width: 26px; height: 26px; }
  .card--back .brand__tagline { font-size: 11px; margin-top: 6px; padding-left: 38px; }
  .holder {
    position: absolute;
    left: 47px; top: 192px;
    margin: 0;
    color: var(--brand-blue);
    font-weight: 700;
    font-size: 19px;
    letter-spacing: 0.8px;
  }
  .contacts {
    position: absolute;
    left: 46px; top: 245px;
    margin: 0; padding: 0;
    list-style: none;
    color: var(--ink);
    font-size: 14px;
  }
  .contacts li {
    display: flex;
    align-items: center;
    height: 20px;
  }
  .contacts svg {
    width: 14px; height: 14px;
    margin-right: 16px;
    fill: var(--ink);
    flex: none;
  }
</style>
</head>
<body>
<main class="stage">

  <section class="card card--front" aria-label="Card front">
    <div class="brand">
      <div class="brand__name">
        <span class="brand__mark"></span>
        <span class="brand__words">NORTHGATE<br>PROPERTY INSPECTIONS</span>
      </div>
      <div class="brand__tagline">The Building and pest expert</div>
    </div>
    <p class="services">Property Inspection | Property Maintenance</p>
  </section>

  <section class="card card--back" aria-label="Card back">
    <div class="brand">
      <div class="brand__name">
        <span class="brand__mark"></span>
        <span class="brand__words">NORTHGATE<br>PROPERTY INSPECTIONS</span>
      </div>
      <div class="brand__tagline">The Building and pest expert</div>
    </div>

    <h2 class="holder">SARAH TILDA</h2>

    <ul class="contacts">
      <li>
        <svg viewBox="0 0 16 16" aria-hidden="true"><path d="M3.5 1l2.5 3-1.5 1.6c.8 2 2.4 3.6 4.4 4.4L10.5 8.5l3 2.5-1.4 2.9C7 13.5 2.5 9 2.1 3.9z"/></svg>
        (02) 5550 1827
      </li>
      <li>
        <svg viewBox="0 0 16 16" aria-hidden="true"><path d="M5 1h6a1 1 0 0 1 1 1v12a1 1 0 0 1-1 1H5a1 1 0 0 1-1-1V2a1 1 0 0 1 1-1zm0 2v9h6V3zm3 10a.8.8 0 1 0 0 .1z"/></svg>
        0400 000 418
      </li>
      <li>
        <svg viewBox="0 0 16 16" aria-hidden="true"><path d="M1 3h14v10H1zm1.5 1.2L8 8.6l5.5-4.4zM2 12h12V5.4L8 10 2 5.4z"/></svg>
        hello@northgateinspect.com.au
      </li>
      <li>
        <svg viewBox="0 0 16 16" aria-hidden="true"><path d="M8 1a7 7 0 1 0 0 14A7 7 0 0 0 8 1zm-1 12.4C4.6 13 3 10.8 3 8c0-.6.1-1.1.3-1.6L6 9v1l1 1zm4.8-1.6c-.2-.6-.8-1-1.4-1H9.5V9a.6.6 0 0 0-.6-.6H5.5V7h1a.6.6 0 0 0 .6-.6V5h1.4a1 1 0 0 0 1-1v-.2a5 5 0 0 1 2.3 8z"/></svg>
        www.northgateinspect.com.au
      </li>
    </ul>
  </section>

</main>
</body>
</html>
```